Business Card Design Project

The business card is for an educational company that provides personalised tuition to students.

The company logo is in orange and blue (as provided) and should be included in the name card design

The philosophy of the company is to make learning a comfortable experience for student as such design of the namecard should look fresh and has a bit of the 'wow' factor. Some of the namecard design that appeals to me are as uploaded under Sample Design.

The particulars that need to be provided are:
(1): Company Name (Quillmont Education)
(1): Name
(2): Educational qualifications which will appear below name
(3): Mobile number
(4): Email address
(5): Website

Industry/Entity Type

Business

Requirements
Must have
• (1): Company Logo

(2): The card background should preferably be coloured both for the front side and back.

(3): The choice of font is important as part of the selection consideration. There is no preferred font that I have selected, designer is free to choose the font that will complement their design.

```html
<!DOCTYPE html>
<html lang="en">
<head>
<meta charset="UTF-8">
<title>Quillmont Education – Business Card</title>
<link rel="stylesheet" href="https://fonts.googleapis.com/css2?family=Libre+Baskerville:wght@700&family=Questrial&display=swap">
<style>
  :root {
    --page-bg: #e9e6e1;
    --orange: #ec8424;
    --orange-deep: #d96d12;
    --blue: #1f7cc8;
    --blue-light: #3aa0e4;
    --blue-deep: #135fa8;
    --card-white: #ffffff;
    --pattern-tint: #f3f3f3;
    --ink: #3b3b3b;
    --ink-soft: #555555;
    --icon-red: #e0502a;
  }
  * { margin: 0; padding: 0; box-sizing: border-box; }
  html, body { width: 1200px; height: 900px; overflow: hidden; }
  body { background: var(--page-bg); position: relative; }

  .card {
    position: absolute;
    width: 560px;
    height: 320px;
    border-radius: 22px;
    overflow: hidden;
    box-shadow: 0 10px 26px rgba(0,0,0,0.18);
  }
  .card-front { left: 60px; top: 110px; background: var(--orange); }
  .card-back  { left: 580px; top: 470px; background: var(--card-white); }

  .front-pattern, .back-pattern { position: absolute; inset: 0; }
  .front-pattern { background: linear-gradient(160deg, var(--orange) 0%, var(--orange-deep) 100%); }
  .back-pattern { background: radial-gradient(ellipse at 55% 50%, var(--pattern-tint) 0%, var(--card-white) 75%); }

  .front-sky { position: absolute; inset: 0; width: 100%; height: 100%; }

  .brand {
    position: absolute;
    display: flex;
    align-items: center;
    gap: 18px;
  }
  .brand-mark { border-radius: 8px; flex: none; }
  .brand-name {
    font-family: "Libre Baskerville", Georgia, serif;
    font-weight: 700;
    line-height: 1.02;
  }
  .card-front .brand { left: 80px; top: 150px; }
  .card-front .brand-mark { width: 70px; height: 70px; background: var(--blue); }
  .card-front .brand-name { color: #ffffff; font-size: 40px; }

  .card-back .brand { left: 40px; top: 130px; }
  .card-back .brand-mark { width: 64px; height: 64px; background: var(--orange); }
  .card-back .brand-name { color: var(--ink); font-size: 32px; }

  .person {
    position: absolute;
    right: 40px;
    top: 38px;
    text-align: left;
    font-family: "Questrial", Arial, sans-serif;
    color: var(--ink);
  }
  .person-name { font-size: 30px; font-variant: small-caps; letter-spacing: 0.5px; }
  .person-role { font-size: 14px; letter-spacing: 1px; color: var(--ink-soft); margin-top: 2px; }

  .contact {
    position: absolute;
    left: 40px;
    bottom: 30px;
    list-style: none;
    font-family: "Questrial", Arial, sans-serif;
    font-size: 19px;
    color: var(--ink);
  }
  .contact li { display: flex; align-items: center; gap: 12px; height: 28px; }
  .contact svg { width: 18px; height: 18px; flex: none; }
</style>
</head>
<body>

<section class="card card-front" aria-label="Card front">
  <div class="front-pattern" role="img" aria-label="Orange damask ornament pattern background"></div>
  <svg class="front-sky" viewBox="0 0 560 320" preserveAspectRatio="none" role="img" aria-label="Blue sky band with a soaring white bird">
    <defs>
      <linearGradient id="skyGrad" x1="0" y1="0" x2="1" y2="1">
        <stop offset="0" stop-color="var(--blue-light)"/>
        <stop offset="1" stop-color="var(--blue-deep)"/>
      </linearGradient>
    </defs>
    <path d="M170 0 H560 V190 C520 130 470 95 400 92 C330 90 260 75 170 0 Z" fill="url(#skyGrad)"/>
  </svg>
  <div class="brand">
    <span class="brand-mark"></span>
    <span class="brand-name">Quillmont<br>Education</span>
  </div>
</section>

<section class="card card-back" aria-label="Card back">
  <div class="back-pattern" role="img" aria-label="Faint grey damask ornament pattern background"></div>

  <div class="person">
    <div class="person-name">Daniel Hartley</div>
    <div class="person-role">PROJECT MANAGER</div>
  </div>

  <div class="brand">
    <span class="brand-mark"></span>
    <span class="brand-name">Quillmont<br>Education</span>
  </div>

  <ul class="contact">
    <li>
      <svg viewBox="0 0 18 18" aria-hidden="true"><rect width="18" height="18" rx="3" fill="var(--icon-red)"/><path d="M5 5.5c0 4 3.5 7.5 7.5 7.5l1-2-2.2-1-1 1c-1.3-.6-2.2-1.5-2.8-2.8l1-1-1-2.2z" fill="#fff"/></svg>
      <span>0198 765 4321</span>
    </li>
    <li>
      <svg viewBox="0 0 18 18" aria-hidden="true"><rect width="18" height="18" rx="3" fill="var(--icon-red)"/><text x="9" y="13" text-anchor="middle" font-family="Arial, sans-serif" font-size="12" fill="#fff">@</text></svg>
      <span>info@quillmonteducation.com</span>
    </li>
    <li>
      <svg viewBox="0 0 18 18" aria-hidden="true"><rect width="18" height="18" rx="3" fill="var(--icon-red)"/><g fill="none" stroke="#fff" stroke-width="1.2"><circle cx="9" cy="9" r="5"/><ellipse cx="9" cy="9" rx="2.2" ry="5"/><path d="M4 9h10"/></g></svg>
      <span>www.quillmonteducation.com</span>
    </li>
  </ul>
</section>

</body>
</html>
```